Velmora Care! Create an exciting flyer for our hemodialysis clinic

Create an engaging Flyer that shows our offering and that will drive patients to our hemodialysis clinic. www.velmoracare.example

Target Market(s)

Mass public

Industry/Entity Type

Healthcare

Requirements
Must have
• 1 Our logo. 2. Should include that we accept all insurances 3. Our tag line “Transforming Lives, One Dialysis Session at a Time.”

```html
<!DOCTYPE html>
<html lang="en">
<head>
<meta charset="utf-8">
<title>Velmora Care – In-Center Hemodialysis Flyer</title>
<link href="https://fonts.googleapis.com/css2?family=Roboto:wght@300;400;500;700;900&display=swap" rel="stylesheet">
<style>
  :root {
    --brand-blue: #1f66ad;
    --brand-blue-deep: #1b5c9e;
    --brand-green: #3fa046;
    --brand-teal: #1d8a86;
    --ink-dark: #333438;
    --ink-body: #4d4f53;
    --panel-grey: #f1f2f3;
    --page-bg: #e9eaeb;
    --white: #ffffff;
  }
  * { box-sizing: border-box; margin: 0; padding: 0; }
  html, body { width: 1200px; height: 641px; overflow: hidden; }
  body {
    background: var(--page-bg);
    font-family: "Roboto", Arial, sans-serif;
    position: relative;
  }
  .flyer {
    position: absolute; left: 352px; top: 0;
    width: 495px; height: 641px;
    background: var(--white);
    overflow: hidden;
  }
  .brand {
    position: absolute; left: 31px; top: 30px;
    display: flex; align-items: center; gap: 10px;
  }
  .brand-square {
    width: 50px; height: 50px;
    background: var(--brand-blue);
  }
  .brand-name {
    font-weight: 700; font-size: 25px; color: var(--brand-blue);
    letter-spacing: 0.5px;
  }
  .hero {
    position: absolute; left: 0; top: 106px; width: 495px; height: 216px;
    background: var(--brand-blue-deep);
  }
  .hero-photo {
    position: absolute; left: 140px; top: 0; width: 355px; height: 211px;
    background: linear-gradient(90deg, var(--brand-blue-deep) 0%, rgba(31,102,173,0.75) 30%, #7fa3ae 60%, #b9c7cc 100%);
  }
  .hero-accent {
    position: absolute; left: 0; bottom: 0; width: 100%; height: 5px;
    background: linear-gradient(90deg, var(--brand-green), var(--brand-teal));
  }
  .tagline {
    position: absolute; left: 30px; top: 20px;
    color: var(--white); font-weight: 900; text-transform: uppercase;
    line-height: 1;
  }
  .tagline .small { display: block; font-size: 22px; letter-spacing: 0.3px; }
  .tagline .big { display: block; font-size: 45px; line-height: 40px; letter-spacing: -0.5px; }
  .tagline .small:first-child { margin-bottom: 4px; }
  .tagline .small:last-child { margin-top: 4px; }
  .photo-strip {
    position: absolute; left: 0; top: 324px; width: 495px; height: 104px;
    display: flex;
  }
  .photo-strip .photo { height: 100%; }
  .photo.nurse { width: 168px; background: linear-gradient(135deg, #cfd8de, #4f86c0); }
  .photo.ward { width: 158px; background: linear-gradient(135deg, #f1f2f2, #c9cdd0); }
  .photo.patient { width: 169px; background: linear-gradient(135deg, #dde3e6, #8d9398); }
  .service {
    position: absolute; left: 27px; top: 440px; width: 236px;
  }
  .service-head { display: flex; align-items: center; gap: 9px; }
  .service-title {
    font-weight: 900; font-size: 21px; line-height: 20px;
    color: var(--brand-blue); text-transform: uppercase;
  }
  .service-rule { margin-top: 10px; height: 1px; background: #9a9ca0; }
  .service-text {
    margin-top: 6px; font-size: 9.3px; line-height: 12.2px; font-weight: 300;
    letter-spacing: -0.1px; color: var(--ink-body);
  }
  .partners {
    position: absolute; left: 287px; top: 428px; width: 208px; height: 178px;
    background: var(--panel-grey);
    padding: 17px 10px 0 28px;
  }
  .partners-text { font-size: 13px; line-height: 14.6px; font-weight: 500; color: var(--ink-body); }
  .partners-places { margin-top: 6px; font-size: 10px; color: var(--ink-body); }
  .footer {
    position: absolute; left: 0; top: 605px; width: 495px; height: 36px;
    background: var(--ink-dark);
    display: flex; align-items: center; gap: 12px; padding-left: 27px;
    color: var(--white); font-size: 10.5px;
    z-index: 1;
  }
  .contact { display: flex; align-items: center; gap: 6px; }
  .insurance {
    position: absolute; left: 287px; top: 559px; width: 208px; height: 65px;
    z-index: 2;
  }
  .insurance svg { position: absolute; inset: 0; width: 100%; height: 100%; }
  .insurance-text {
    position: absolute; left: 49px; top: 13px;
    color: var(--white); font-weight: 900; font-size: 18.5px; line-height: 19.5px;
    text-transform: uppercase;
  }
</style>
</head>
<body>
  <main class="flyer">
    <div class="brand">
      <div class="brand-square"></div>
      <span class="brand-name">Velmora Care</span>
    </div>

    <section class="hero">
      <div class="hero-photo" role="img" aria-label="Clinician checking on a patient resting in a hospital bed during dialysis"></div>
      <h1 class="tagline">
        <span class="small">Transforming</span>
        <span class="big">Lives,</span>
        <span class="big">One</span>
        <span class="big">Dialysis</span>
        <span class="small">Session at a time</span>
      </h1>
      <div class="hero-accent"></div>
    </section>

    <section class="photo-strip">
      <div class="photo nurse" role="img" aria-label="Nurse in scrubs operating a dialysis machine"></div>
      <div class="photo ward" role="img" aria-label="Bright dialysis ward with treatment beds"></div>
      <div class="photo patient" role="img" aria-label="Patient resting in a treatment bed"></div>
    </section>

    <section class="service">
      <div class="service-head">
        <svg width="30" height="36" viewBox="0 0 30 36" fill="none" stroke="#1f66ad" stroke-width="1.6" aria-hidden="true">
          <rect x="8" y="2" width="18" height="14" rx="1.5"/>
          <rect x="11" y="5" width="12" height="7"/>
          <rect x="8" y="18" width="18" height="16" rx="1.5"/>
          <circle cx="13" cy="24" r="1.2"/><circle cx="17" cy="24" r="1.2"/><circle cx="21" cy="24" r="1.2"/>
          <line x1="12" y1="29" x2="22" y2="29"/>
          <path d="M8 8 H3 V26 H8"/>
        </svg>
        <h2 class="service-title">In-Center<br>Hemodialysis</h2>
      </div>
      <div class="service-rule"></div>
      <p class="service-text">We offer In-center hemodialysis for renal patients who prefer to have their treatments at a dialysis center. Our dialysis center has 6 Halvern dialysis machines, supported by our state of the art water purification system. Pick up and drop off of patients is an additional service we offer for all in-center hemodialysis patients. Call us now for more information!</p>
    </section>

    <aside class="partners">
      <p class="partners-text">Once you're a Dialysis Patient with Velmora, you can also Dialyze at any or Our Partner Locations in Trinidad</p>
      <p class="partners-places">(Chaguanas and Piarco)</p>
    </aside>

    <footer class="footer">
      <span class="contact">
        <svg width="11" height="8" viewBox="0 0 11 8" aria-hidden="true"><rect width="11" height="8" fill="#3fa046"/><path d="M0 0 L5.5 4.5 L11 0" stroke="#333438" stroke-width="1.2" fill="none"/></svg>
        info@velmoracare.example
      </span>
      <span class="contact">
        <svg width="10" height="10" viewBox="0 0 24 24" aria-hidden="true"><path fill="#3fa046" d="M6.6 10.8a15.1 15.1 0 0 0 6.6 6.6l2.2-2.2a1 1 0 0 1 1-.25 11.4 11.4 0 0 0 3.6.57 1 1 0 0 1 1 1V20a1 1 0 0 1-1 1A17 17 0 0 1 3 4a1 1 0 0 1 1-1h3.5a1 1 0 0 1 1 1c0 1.25.2 2.45.57 3.57a1 1 0 0 1-.25 1z"/></svg>
        868-555-0142
      </span>
    </footer>

    <div class="insurance">
      <svg viewBox="0 0 208 65" preserveAspectRatio="none" aria-hidden="true">
        <defs>
          <linearGradient id="insuranceFill" x1="0" x2="1" y1="0" y2="0">
            <stop offset="0" stop-color="#1f66ad"/>
            <stop offset="1" stop-color="#1d8a86"/>
          </linearGradient>
        </defs>
        <polygon points="30,0 208,0 208,65 25,65 0,40" fill="url(#insuranceFill)"/>
      </svg>
      <p class="insurance-text">Accept all<br>insurances</p>
    </div>
  </main>
</body>
</html>
```